Very basic draft completed. Need someone to apply their creative magic

I am building a new website for my business and looking for a designer to assist me on a part-time basis.

My business is a booking site for classes and lessons. It is essentially a directory service, and needs to conform to a standard web-layout that is easy to navigate and familiar to users (i.e. nothing to creative). The function and structure i have adopted is common amongst sites like qumo, hotel booking services, etc.

The first task on my list is to develop the main page. I have already compiled a draft of the first page using Fireworks (see attached) and am looking for someone to cast their creative magic to this draft while maintaining the general layout of the page. After the main page is developed, I will be looking for the same designer to assist with the rest of the site.

Design wise, I'd like to go for a slightly retro feel
By this I mean a moderately modern page with a spark of retro here and there. If you look at my draft you'll notice that I've used regular font for most text, and retro/old-school fonts for surburb names.

I happy for you to suggest colours, but regular page elements such as web links need to remain standard (i.e links = blue) so that they are familiar and identifiable to my users.

Other points:
1) I don't want the page to be too dark (dark headings, images and borders are fine, but I'd like to maintain white or light backgrounds)

2) Positioning: The Body should be centred, with the Header and Footer extending across the hole screen (as illustrated in my draft)

3) I'm happy if the design includes images from photostock libraries.The Silhoute picture for my draft were choosen because there are hundreds of them, and I can regularly change them on the site - keeping it fresh and new. I'd be very happy if the design incorporate images that could also be place often using photo stock images (i.e. happy to keep silhoutes, but leave it to you to decide what looks best)

Note: I'm happy for you to "copy" art work from any photo stock site, and I will pay for the full quality images when the design is selected.

4) The page Footer needs a lot of attention. It will contain standard Footer links/elements.

5) You are free to do anything to the Header section. It needs to have login/register elements

I'm happy to provide further comments, or review other sites/work to help direct design work.

Hi All,

I've updated the project brief, eliminating many of the requirements and giving you the freedom with design submissions, etc. I've also added the $20 payment for submissions. 
Cheers,
Corwin

Reason: I'm away on holiday and will review your submissions and provide feedback when I get back.

```html
<!DOCTYPE html>
<html lang="en">
<head>
<meta charset="utf-8">
<title>Lumio Classes – Featured Classes &amp; Activities</title>
<link rel="stylesheet" href="https://fonts.googleapis.com/css2?family=Roboto:wght@300;400;500&display=swap">
<style>
:root{
  --bar:#555658;
  --bar-text:#d8d8d8;
  --panel:#ffffff;
  --ink:#333333;
  --muted:#8a8a8a;
  --accent:#f26a10;
  --link:#2a7fb8;
  --green-a:#8fc641;
  --green-b:#5fa52c;
  --red-a:#e02a1c;
  --red-b:#f4621e;
  --blue-a:#2f8fc4;
  --blue-b:#56b9e2;
  --line:#dcdcdc;
}
*{box-sizing:border-box;margin:0;padding:0}
html,body{width:1200px;height:1082px;overflow:hidden}
body{position:relative;font-family:"Roboto",Arial,sans-serif;color:var(--ink);
  background:linear-gradient(135deg,#e4e4e4 0%,#f4f4f4 45%,#e6e6e6 100%)}
.abs{position:absolute}

/* top bar */
.topbar{left:0;top:0;width:1200px;height:30px;background:var(--bar);color:var(--bar-text);font-size:10.5px}
.topbar .item{position:absolute;top:9px;white-space:nowrap}
.topbar svg{position:absolute}
.search-field{position:absolute;left:608px;top:5px;width:194px;height:19px;background:#fff;border:1px solid #bbb;font-size:10.5px;color:#999;padding:3px 8px;line-height:12px}

/* page panel */
.page{left:184px;top:38px;width:832px;height:1044px;background:var(--panel);box-shadow:0 0 4px rgba(0,0,0,.12)}

.brand{left:198px;top:72px;font-size:28px;font-weight:400;color:#333;line-height:1;white-space:nowrap}

.band{height:28px;color:#fff;font-size:14px;line-height:28px;padding-left:10px;box-shadow:0 2px 2px rgba(0,0,0,.15)}
.band.explore{left:195px;top:126px;width:124px;background:linear-gradient(90deg,var(--green-a),var(--green-b))}
.band.showing{left:332px;top:126px;width:530px;background:linear-gradient(90deg,var(--red-a),var(--red-b) 60%,var(--red-a))}
.band.schedule{left:876px;top:126px;width:130px;background:linear-gradient(90deg,var(--blue-a),var(--blue-b))}
.sort{position:absolute;right:10px;top:3px;width:164px;height:21px;background:#d8301c;border:1px solid #c32515;font-size:11.5px;line-height:19px;padding-left:18px}
.sort svg{position:absolute;right:6px;top:7px}

/* categories */
.cats{left:195px;top:166px;list-style:none;font-size:10px;line-height:15px}
.cats li{padding-left:11px;position:relative;color:#333}
.cats li.arrow::before{content:"";position:absolute;left:1px;top:3px;border-left:5px solid #999;border-top:4px solid transparent;border-bottom:4px solid transparent}
.cats li.open::before{content:"";position:absolute;left:0;top:5px;border-top:5px solid #999;border-left:4px solid transparent;border-right:4px solid transparent}
.cats li.sub{color:var(--muted)}
.cats li.sub.current{color:#222}

.results-note{left:333px;top:166px;font-size:10px;color:var(--muted)}

/* cards */
.card{left:332px;width:530px;height:110px;background:#fff;border:1px solid #e2e2e2;box-shadow:0 1px 3px rgba(0,0,0,.15)}
.card .photo{position:absolute;left:13px;top:11px;width:125px;height:84px;background:linear-gradient(120deg,#d9992e 0%,#3b2a4a 35%,#8a1a1a 55%,#e8c35a 75%,#9bb03c 100%)}
.card .title{position:absolute;left:150px;top:10px;font-size:12.5px;color:#222;letter-spacing:.2px}
.card .host{position:absolute;left:150px;top:26px;font-size:9.5px;color:var(--accent)}
.card .addr,.card .times{position:absolute;left:150px;font-size:9.5px;color:#333;padding-left:17px;white-space:nowrap}
.card .addr{top:40px}.card .times{top:54px}
.card .addr svg,.card .times svg{position:absolute;left:0;top:0}
.card .hl{color:var(--accent)}
.card .desc{position:absolute;left:150px;top:70px;width:270px;font-size:9.5px;line-height:12.5px;color:var(--muted);white-space:nowrap}
.card .next{position:absolute;right:15px;top:12px;text-align:right;font-size:7.5px;color:#333}
.card .next b{display:block;font-weight:400;font-size:9.5px;color:var(--accent);margin-top:2px}
.card .price{position:absolute;right:15px;top:68px;text-align:right;font-size:7.5px;color:#333;line-height:1}
.card .price b{display:block;font-weight:300;font-size:25px;color:var(--accent)}

/* schedule */
.sched-head{left:884px;font-size:11.5px;color:var(--muted)}
.checks{left:885px;list-style:none;font-size:10px;line-height:15px}
.checks li{padding-left:19px;position:relative}
.checks li::before{content:"";position:absolute;left:0;top:2px;width:9px;height:9px;border:1px solid #aaa;background:#fff}
.checks li.active{color:var(--link)}
.update{left:905px;top:449px;width:68px;height:23px;background:linear-gradient(180deg,var(--blue-b),var(--blue-a));color:#fff;font-size:13px;text-align:center;line-height:23px;box-shadow:0 1px 2px rgba(0,0,0,.3)}

/* footer */
.footer-rule{left:192px;top:1020px;width:808px;height:1px;background:var(--line)}
.footer{top:1026px;font-size:10px;color:var(--muted)}
</style>
</head>
<body>

<header class="abs topbar">
  <svg style="left:196px;top:7px" width="16" height="14" viewBox="0 0 16 14"><path d="M8 1L1 7h2v6h4V9h2v4h4V7h2z" fill="#cfcfcf"/></svg>
  <span class="item" style="left:219px">HOME</span>
  <svg style="left:287px;top:7px" width="16" height="15" viewBox="0 0 16 15"><rect x="1" y="2" width="14" height="12" fill="none" stroke="#cfcfcf"/><path d="M1 5h14M4 8h2M7 8h2M10 8h2M4 11h2M7 11h2M10 11h2" stroke="#cfcfcf"/></svg>
  <span class="item" style="left:313px">what's on TODAY &nbsp;| &nbsp;TOMORROW &nbsp;| &nbsp;THIS WEEK</span>
  <div class="search-field">keyword</div>
  <svg style="left:806px;top:6px" width="19" height="18" viewBox="0 0 19 18"><circle cx="7" cy="7" r="5" fill="none" stroke="#ddd" stroke-width="2"/><path d="M11 11l6 5" stroke="#ddd" stroke-width="3"/></svg>
  <span class="item" style="left:834px">SEARCH</span>
  <span class="item" style="left:936px">Sign In &nbsp;| &nbsp;Join</span>
</header>

<div class="abs page"></div>

<div class="abs brand">Lumio Classes</div>

<div class="abs band explore">EXPLORE</div>
<div class="abs band showing">SHOWING: Featured Classes &amp; Activities
  <div class="sort">Sort by: Last Updated
    <svg width="10" height="7" viewBox="0 0 10 7"><path d="M0 0h10L5 7z" fill="#fff"/></svg>
  </div>
</div>
<div class="abs band schedule">SCHEDULE</div>

<ul class="abs cats">
  <li class="arrow">Creative Arts &amp; Crafts</li>
  <li class="arrow">Food &amp; Wine</li>
  <li class="arrow">Health &amp; Fitness</li>
  <li class="arrow">Languages &amp; Culture</li>
  <li class="arrow">Music</li>
  <li class="open">Sports &amp; Outdoors</li>
  <li class="sub">Martial Arts (11)</li>
  <li class="sub">Pilates (9)</li>
  <li class="sub current">Swimwz2)</li>
  <li class="sub">Tennis (3)</li>
  <li class="arrow">Teens &amp; Young Adults</li>
</ul>

<div class="abs results-note">Displaying 6 result(s) for Featured Classes &amp; Activities</div>

<article class="abs card" style="top:189px">
  <div class="photo" role="img" aria-label="Photo of cheese, grapes and red wine glasses"></div>
  <div class="title">PAIRING WINE WITH CHEESE</div>
  <div class="host">with The Larder Room</div>
  <div class="addr"><svg width="12" height="11" viewBox="0 0 12 11"><path d="M2 1l8 8M6 1l-3 5h6z" stroke="#555" fill="#555"/></svg>48/210 Harbour Lane, <span class="hl">Melbourne</span> VIC 3000</div>
  <div class="times"><svg width="12" height="11" viewBox="0 0 12 11"><rect x="1" y="2" width="10" height="8" fill="none" stroke="#555"/><path d="M1 4h10" stroke="#555"/></svg>Friday: <span class="hl">2:00pm</span> &nbsp;| &nbsp;Sunday: <span class="hl">2:00pm</span></div>
  <div class="desc">Do you love cheese and wine? Here's a perfect chance<br>to sit and taste how cheese and change... &nbsp;&nbsp;more</div>
  <div class="next">Next available<b>Monday 20th August</b></div>
  <div class="price">From<b>$30</b></div>
</article>

<article class="abs card" style="top:313px">
  <div class="photo" role="img" aria-label="Photo of cheese, grapes and red wine glasses"></div>
  <div class="title">PAIRING WINE WITH CHEESE</div>
  <div class="host">with The Larder Room</div>
  <div class="addr"><svg width="12" height="11" viewBox="0 0 12 11"><path d="M2 1l8 8M6 1l-3 5h6z" stroke="#555" fill="#555"/></svg>48/210 Harbour Lane, <span class="hl">Melbourne</span> VIC 3000</div>
  <div class="times"><svg width="12" height="11" viewBox="0 0 12 11"><rect x="1" y="2" width="10" height="8" fill="none" stroke="#555"/><path d="M1 4h10" stroke="#555"/></svg>Friday: <span class="hl">2:00pm</span> &nbsp;| &nbsp;Sunday: <span class="hl">2:00pm</span></div>
  <div class="desc">Do you love cheese and wine? Here's a perfect chance<br>to sit and taste how cheese and change... &nbsp;&nbsp;more</div>
  <div class="next">Next available<b>Monday 20th August</b></div>
  <div class="price">From<b>$30</b></div>
</article>

<article class="abs card" style="top:440px">
  <div class="photo" role="img" aria-label="Photo of cheese, grapes and red wine glasses"></div>
  <div class="title">PAIRING WINE WITH CHEESE</div>
  <div class="host">with The Larder Room</div>
  <div class="addr"><svg width="12" height="11" viewBox="0 0 12 11"><path d="M2 1l8 8M6 1l-3 5h6z" stroke="#555" fill="#555"/></svg>48/210 Harbour Lane, <span class="hl">Melbourne</span> VIC 3000</div>
  <div class="times"><svg width="12" height="11" viewBox="0 0 12 11"><rect x="1" y="2" width="10" height="8" fill="none" stroke="#555"/><path d="M1 4h10" stroke="#555"/></svg>Friday: <span class="hl">2:00pm</span> &nbsp;| &nbsp;Sunday: <span class="hl">2:00pm</span></div>
  <div class="desc">Do you love cheese and wine? Here's a perfect chance<br>to sit and taste how cheese and change... &nbsp;&nbsp;more</div>
  <div class="next">Next available<b>Monday 20th August</b></div>
  <div class="price">From<b>$30</b></div>
</article>

<article class="abs card" style="top:564px">
  <div class="photo" role="img" aria-label="Photo of cheese, grapes and red wine glasses"></div>
  <div class="title">PAIRING WINE WITH CHEESE</div>
  <div class="host">with The Larder Room</div>
  <div class="addr"><svg width="12" height="11" viewBox="0 0 12 11"><path d="M2 1l8 8M6 1l-3 5h6z" stroke="#555" fill="#555"/></svg>48/210 Harbour Lane, <span class="hl">Melbourne</span> VIC 3000</div>
  <div class="times"><svg width="12" height="11" viewBox="0 0 12 11"><rect x="1" y="2" width="10" height="8" fill="none" stroke="#555"/><path d="M1 4h10" stroke="#555"/></svg>Friday: <span class="hl">2:00pm</span> &nbsp;| &nbsp;Sunday: <span class="hl">2:00pm</span></div>
  <div class="desc">Do you love cheese and wine? Here's a perfect chance<br>to sit and taste how cheese and change... &nbsp;&nbsp;more</div>
  <div class="next">Next available<b>Monday 20th August</b></div>
  <div class="price">From<b>$30</b></div>
</article>

<article class="abs card" style="top:688px">
  <div class="photo" role="img" aria-label="Photo of cheese, grapes and red wine glasses"></div>
  <div class="title">PAIRING WINE WITH CHEESE</div>
  <div class="host">with The Larder Room</div>
  <div class="addr"><svg width="12" height="11" viewBox="0 0 12 11"><path d="M2 1l8 8M6 1l-3 5h6z" stroke="#555" fill="#555"/></svg>48/210 Harbour Lane, <span class="hl">Melbourne</span> VIC 3000</div>
  <div class="times"><svg width="12" height="11" viewBox="0 0 12 11"><rect x="1" y="2" width="10" height="8" fill="none" stroke="#555"/><path d="M1 4h10" stroke="#555"/></svg>Friday: <span class="hl">2:00pm</span> &nbsp;| &nbsp;Sunday: <span class="hl">2:00pm</span></div>
  <div class="desc">Do you love cheese and wine? Here's a perfect chance<br>to sit and taste how cheese and change... &nbsp;&nbsp;more</div>
  <div class="next">Next available<b>Monday 20th August</b></div>
  <div class="price">From<b>$30</b></div>
</article>

<article class="abs card" style="top:812px">
  <div class="photo" role="img" aria-label="Photo of cheese, grapes and red wine glasses"></div>
  <div class="title">PAIRING WINE WITH CHEESE</div>
  <div class="host">with The Larder Room</div>
  <div class="addr"><svg width="12" height="11" viewBox="0 0 12 11"><path d="M2 1l8 8M6 1l-3 5h6z" stroke="#555" fill="#555"/></svg>48/210 Harbour Lane, <span class="hl">Melbourne</span> VIC 3000</div>
  <div class="times"><svg width="12" height="11" viewBox="0 0 12 11"><rect x="1" y="2" width="10" height="8" fill="none" stroke="#555"/><path d="M1 4h10" stroke="#555"/></svg>Friday: <span class="hl">2:00pm</span> &nbsp;| &nbsp;Sunday: <span class="hl">2:00pm</span></div>
  <div class="desc">Do you love cheese and wine? Here's a perfect chance<br>to sit and taste how cheese and change... &nbsp;&nbsp;more</div>
  <div class="next">Next available<b>Monday 20th August</b></div>
  <div class="price">From<b>$30</b></div>
</article>

<div class="abs sched-head" style="top:166px">Day</div>
<ul class="abs checks" style="top:189px">
  <li class="active">Monday</li><li>Tuesday</li><li>Wednesday</li><li>Thursday</li>
  <li>Friday</li><li>Saturday</li><li>Sunday</li><li>All</li>
</ul>
<div class="abs sched-head" style="top:322px">Time</div>
<ul class="abs checks" style="top:345px">
  <li>Dawn (6-9am)</li><li>Morning (9-12pm)</li><li>Midday (12-3pm)</li>
  <li>Afternoon (3-6pm)</li><li>Evening (6-12am)</li><li>All</li>
</ul>
<div class="abs update">Update</div>

<div class="abs footer-rule"></div>
<div class="abs footer" style="left:192px">Lumio Classes Pty Ltd &nbsp;&nbsp;&nbsp;ACN 000 111 222</div>
<div class="abs footer" style="left:883px">About Us</div>
<div class="abs footer" style="left:949px">Contact Us</div>

</body>
</html>
```